New banner graphics for Kelbro.com website

I've developed a software tool that helps businesses ensure they are working on their most valuable and important work.

I would like a banner graphic for my home page (www.kelbro.com) that can somehow capture the value of focus and intentional outcomes.

I had an initial thought of a starry sky that shifts focus to a few bright stars, but while that might sound ok, I think my idea is lame hence I'm coming to you guys.

My sites two primary colors are a soft purple and gray.
#919EC1(purple)
#9E9E9E (gray)

Target Market(s)

B2B for enterprises. Typical customers are CFOs, CIOs/Heads of IT

Industry/Entity Type

Business Software

Number of Pages Required

1 page

Font styles to use
Sans Serif

Colors
b8a6cd
cedeed

Requirements
Must have
• I use Divi as my Wordpress theme and the current main landing page can be seen at www.kelbro.com.
• My logo colors are:
• #919EC1(purple)
• #9E9E9E (gray)
Should not have
• Lots of distraction or visual "noise". I want to re-enforce the message that my software is focused on their business and not my products or website.

```html
<!DOCTYPE html>
<html lang="en">
<head>
<meta charset="utf-8">
<title>Kelbro – Keystone strategy software</title>
<link rel="stylesheet" href="https://fonts.googleapis.com/css2?family=Mulish:wght@400;500;600&family=Open+Sans:wght@400;600&display=swap">
<style>
:root{
  --purple:#b8a6cd;
  --purple-deep:#a48fc3;
  --purple-title:#9d87c4;
  --sky:#cedeed;
  --brand-purple:#919ec1;
  --gray:#9e9e9e;
  --text:#6d6d6d;
  --text-dark:#333;
  --band-gray:#efefef;
  --footer:#000;
  --white:#fff;
  --demo-btn:#c9d6e8;
}
*{margin:0;padding:0;box-sizing:border-box}
html,body{width:1200px;height:2808px;overflow:hidden;background:var(--white)}
body{position:relative;font-family:"Open Sans",Arial,sans-serif;color:var(--text)}
.abs{position:absolute}
h1,h2,h3,.heading{font-family:"Mulish","Open Sans",sans-serif;font-weight:500}

/* hero */
.hero{left:0;top:0;width:1200px;height:660px;overflow:hidden}
.hero-photo{position:absolute;inset:0;background:linear-gradient(180deg,#2d5fae 0%,#5a86c6 30%,#a9bfd8 48%,#8a93a3 62%,#6e6656 80%,#8a6b47 100%)}
.hero-wave{position:absolute;left:0;bottom:0}
.brand{left:120px;top:26px;font-family:"Mulish",sans-serif;font-size:50px;font-weight:400;color:var(--white);letter-spacing:1px}
.nav{top:47px;left:470px;display:flex;gap:0;font-family:"Mulish",sans-serif;font-size:18px;color:var(--white)}
.nav a{color:inherit;text-decoration:none;position:absolute;white-space:nowrap}
.login{left:979px;top:37px;width:104px;height:39px;border:2px solid var(--white);color:var(--white);font-family:"Mulish",sans-serif;font-size:18px;text-align:center;line-height:35px}
.hero-title{left:122px;top:253px;font-size:38px;color:var(--white);font-weight:600}
.hero-text{left:122px;top:314px;width:460px;font-size:18.5px;line-height:25px;color:var(--white)}
.hero-btn{left:122px;top:419px;width:183px;height:44px;background:var(--purple);color:var(--white);font-family:"Mulish",sans-serif;font-size:18px;line-height:44px;text-align:center}
.dots{left:588px;top:577px;display:flex;gap:7px}
.dots span{width:13px;height:13px;border-radius:50%;background:var(--white);border:2px solid var(--white)}
.dots span.off{background:transparent}

/* intro */
.intro-title{left:125px;top:746px;font-size:31px;color:var(--purple-title);font-weight:600}
.intro-lead{left:128px;top:798px;width:390px;font-size:17px;line-height:23px;color:var(--text)}
.intro-body{left:128px;top:857px;width:440px;font-size:12.5px;line-height:20px;color:var(--gray)}
.benefits{font-size:14.5px;color:var(--text);list-style:none}
.benefits li{position:absolute;white-space:nowrap}
.benefits li::before{content:"›";margin-right:9px;color:var(--gray)}
.video{left:588px;top:752px;width:494px;height:308px;background:radial-gradient(ellipse at center,#4a4a4a 0%,#262626 100%)}
.video-label{position:absolute;left:0;right:0;top:18px;text-align:center;font-style:italic;font-size:25px;color:#bdbdbd}
.video-screen{position:absolute;left:76px;top:60px;width:325px;height:204px;border:3px solid #b5b5b5;background:radial-gradient(ellipse at center,#2e56a8 0%,#17306e 100%)}
.video-name{position:absolute;left:0;right:0;top:68px;text-align:center;font-family:"Mulish",sans-serif;font-weight:600;font-size:44px;color:#b9b9b9;letter-spacing:1px}
.video-play{position:absolute;left:121px;top:57px}

/* differences */
.diff{left:0;top:1138px;width:1200px;height:492px;background:linear-gradient(180deg,var(--sky) 0%,#c4c6e2 45%,var(--purple) 100%)}
.diff-title{position:absolute;left:0;right:0;top:44px;text-align:center;font-size:32px;color:var(--white);font-weight:600}
.feature{position:absolute;width:360px}
.feature svg{position:absolute;left:0;top:0}
.feature h3{position:absolute;left:116px;top:0;font-size:23px;color:var(--white);font-weight:500;white-space:nowrap}
.feature p{position:absolute;left:116px;top:36px;width:345px;font-size:13.5px;line-height:20px;color:var(--white)}

/* testimonials */
.testi{left:0;top:1630px;width:1200px;height:384px;background:var(--band-gray)}
.testi-title{position:absolute;left:0;right:0;top:46px;text-align:center;font-size:32px;color:var(--text-dark);font-weight:400}
.quote{position:absolute;left:307px;top:102px;width:605px;height:166px;background:var(--purple)}
.quote p{position:absolute;left:80px;right:80px;top:40px;text-align:center;font-size:16px;line-height:26px;color:var(--white)}
.quote .mark{position:absolute;font-family:Georgia,serif;font-size:80px;color:#cdc0dc;line-height:1}
.author{position:absolute;left:0;right:0;top:280px;text-align:center;font-family:"Mulish",sans-serif;font-size:18px;line-height:28px;color:#111}
.arrow{position:absolute;top:158px}

/* demo */
.chart{left:146px;top:2078px}
.demo-title{left:575px;top:2080px;font-size:32px;color:var(--text-dark);font-weight:400}
.demo-text{left:575px;top:2138px;width:500px;font-size:13.5px;line-height:24px;color:var(--gray)}
.demo-btn{left:575px;top:2286px;width:136px;height:39px;background:var(--demo-btn);color:var(--white);font-size:13px;font-weight:600;line-height:39px;text-align:center}

/* footer */
.footer{left:0;top:2415px;width:1200px;height:393px;background:var(--footer);color:var(--white)}
.footer h4{position:absolute;top:70px;font-family:"Mulish",sans-serif;font-weight:400;font-size:21px}
.footer ul{list-style:none;position:absolute;top:120px;font-size:15px;line-height:30.5px}
.contact{position:absolute;left:797px;top:117px;font-size:15px;line-height:30.5px}
.contact div{display:flex;align-items:center;gap:10px}
.contact svg{flex:none}
.social{position:absolute;left:558px;top:114px;display:flex;gap:7px}
.social span{width:39px;height:39px;border:2px solid var(--white);border-radius:50%}
.footer-rule{position:absolute;left:131px;top:318px;width:951px;height:1px;background:#444}
.copyright{position:absolute;left:0;right:0;top:340px;text-align:center;font-size:11.5px;color:#8a8a8a}
</style>
</head>
<body>

<section class="abs hero">
  <div class="hero-photo" role="img" aria-label="Hiker with backpack standing on a rocky ridge looking at snowy mountain peaks under a blue sky"></div>
  <svg class="hero-wave" width="1200" height="120" viewBox="0 0 1200 120" aria-hidden="true">
    <path d="M0 120 L0 108 C220 60 420 40 640 58 C860 76 1040 72 1200 40 L1200 120 Z" fill="#fff"/>
  </svg>
</section>

<div class="abs brand">kelbro</div>
<nav class="abs nav">
  <a style="left:0">Request a Demo</a>
  <a style="left:169px">About</a>
  <a style="left:257px">Pricing</a>
  <a style="left:347px">FAQ</a>
  <a style="left:416px">Support</a>
</nav>
<div class="abs login">Log In</div>

<h1 class="abs hero-title">Is Your Business Strategy</h1>
<p class="abs hero-text">Written down or loose thoughts – on the best of days. Driving projects or just a set of slides tacked to walls Shared with the team</p>
<div class="abs hero-btn">Get Started&nbsp; ›</div>
<div class="abs dots"><span class="off"></span><span></span><span></span><span></span></div>

<h2 class="abs intro-title">Get KEYSTONE</h2>
<p class="abs intro-lead">A simple software tool that makes your business goals actionable.</p>
<p class="abs intro-body">Even if you've never felt comfortable defining your business strategy, Keystone is for you. It's simple to use, easy to understand, and keeps you focused on outcomes.</p>
<ul class="benefits">
  <li style="left:139px;top:943px">Define the Outcomes</li>
  <li style="left:139px;top:975px">Set the Direction</li>
  <li style="left:139px;top:1006px">Focus the Resources</li>
  <li style="left:346px;top:943px">Reduce the Risk</li>
  <li style="left:346px;top:975px">Increase Team Engagement</li>
</ul>

<div class="abs video" role="img" aria-label="Introductory video for Keystone">
  <div class="video-label">Introducing</div>
  <div class="video-screen">
    <div class="video-name">KEYSTONE</div>
    <svg class="video-play" width="84" height="84" viewBox="0 0 84 84" aria-hidden="true">
      <circle cx="42" cy="42" r="38" fill="none" stroke="#fff" stroke-width="5"/>
      <path d="M33 25 L60 42 L33 59 Z" fill="#fff"/>
    </svg>
  </div>
</div>

<section class="abs diff">
  <h2 class="diff-title">What Makes Keystone Different?</h2>

  <div class="feature" style="left:146px;top:135px">
    <svg width="106" height="100" viewBox="0 0 106 100" aria-hidden="true">
      <path d="M27 2 H79 L104 50 L79 98 H27 L2 50 Z" fill="none" stroke="#fff" stroke-width="2"/>
      <circle cx="53" cy="50" r="22" fill="none" stroke="#fff" stroke-width="3"/>
      <path d="M42 50 L51 59 L70 38" fill="none" stroke="#fff" stroke-width="4"/>
    </svg>
    <h3>Ease of Use</h3>
    <p>We want you to spend time thinking about and planning for your organization's success, not learning yet another tool. Keystone has a modern UI making it more intuitive.</p>
  </div>

  <div class="feature" style="left:618px;top:135px">
    <svg width="106" height="100" viewBox="0 0 106 100" aria-hidden="true">
      <path d="M27 2 H79 L104 50 L79 98 H27 L2 50 Z" fill="none" stroke="#fff" stroke-width="2"/>
      <circle cx="53" cy="50" r="22" fill="none" stroke="#fff" stroke-width="2"/>
      <circle cx="53" cy="50" r="14" fill="none" stroke="#fff" stroke-width="2"/>
      <circle cx="53" cy="50" r="6" fill="none" stroke="#fff" stroke-width="2"/>
    </svg>
    <h3>Focus on Outcomes</h3>
    <p>Gain alignment with other leaders and team members early by building, shaping and working towards a shared vision of success.</p>
  </div>

  <div class="feature" style="left:146px;top:309px">
    <svg width="106" height="100" viewBox="0 0 106 100" aria-hidden="true">
      <path d="M27 2 H79 L104 50 L79 98 H27 L2 50 Z" fill="none" stroke="#fff" stroke-width="2"/>
      <circle cx="53" cy="50" r="16" fill="none" stroke="#fff" stroke-width="2"/>
      <path d="M53 26 V74 M29 50 H77 M38 35 L68 65 M68 35 L38 65" stroke="#fff" stroke-width="2"/>
    </svg>
    <h3>Practical Approach</h3>
    <p>Getting started is easier when you aren't worried about an overly sophisticated framework or academic model.</p>
  </div>

  <div class="feature" style="left:618px;top:309px">
    <svg width="106" height="100" viewBox="0 0 106 100" aria-hidden="true">
      <path d="M27 2 H79 L104 50 L79 98 H27 L2 50 Z" fill="none" stroke="#fff" stroke-width="2"/>
      <circle cx="60" cy="40" r="9" fill="none" stroke="#fff" stroke-width="6" stroke-dasharray="4 3"/>
      <circle cx="60" cy="40" r="4" fill="#fff"/>
      <path d="M30 62 H44 L56 66 H70 L78 58" fill="none" stroke="#fff" stroke-width="3"/>
    </svg>
    <h3>Support of Industry Frameworks</h3>
    <p>While Keystone has been designed to be comfortable for all business leaders, it ties well to industry frameworks.</p>
  </div>
</section>

<section class="abs testi">
  <h2 class="testi-title">Testimonials</h2>
  <svg class="arrow" style="left:221px" width="24" height="60" viewBox="0 0 24 60" aria-hidden="true"><path d="M22 2 L2 30 L22 58" fill="none" stroke="#888" stroke-width="2"/></svg>
  <div class="quote">
    <span class="mark" style="left:28px;top:32px">“</span>
    <p>Keystone brings the fanciful world of strategic planning down to earth, and fits practitioners of modern agile management practices.</p>
    <span class="mark" style="right:28px;top:66px">”</span>
  </div>
  <svg class="arrow" style="left:966px" width="24" height="60" viewBox="0 0 24 60" aria-hidden="true"><path d="M2 2 L22 30 L2 58" fill="none" stroke="#888" stroke-width="2"/></svg>
  <div class="author">Arvind<br>CEO, IT Services</div>
</section>

<svg class="abs chart" width="390" height="262" viewBox="0 0 390 262" role="img" aria-label="Line chart trending upward">
  <defs>
    <pattern id="grid" width="20" height="20" patternUnits="userSpaceOnUse">
      <path d="M20 0 H0 V20" fill="none" stroke="#d4e6f2" stroke-width="1"/>
    </pattern>
  </defs>
  <rect width="390" height="262" fill="#f3f8fc"/>
  <rect width="390" height="262" fill="url(#grid)"/>
  <path d="M0 182 L52 148 L72 160 L92 168 L130 118 L140 152 L150 140 L180 146 L232 88 L258 86 L282 70 L330 30" fill="none" stroke="#1aa7dc" stroke-width="6" stroke-linejoin="round"/>
  <path d="M350 12 L318 20 L336 42 Z" fill="#1aa7dc"/>
</svg>
<h2 class="abs demo-title">Request a Demo</h2>
<p class="abs demo-text">Maecenas aliquet velit vel turpis Mauris neque metus malesuada nec ultricies sit amet porttitor mattis enim In massa libero interdum nec interdum vel blandit sed nulla In ullamcorper est eget tempor cursus neque mi consectetuer mi a ultricies massa est sed nisl Class aptent taciti sociosqu ad litora torquent per conubia nostra per</p>
<div class="abs demo-btn">CLICK HERE</div>

<footer class="abs footer">
  <h4 style="left:122px">Company</h4>
  <ul style="left:122px"><li>Resources</li><li>Chronicles</li><li>Support</li><li>FAQ</li></ul>
  <h4 style="left:343px">Resources</h4>
  <ul style="left:343px"><li>Terms of Service</li><li>Pricing</li><li>About</li></ul>
  <h4 style="left:560px">Follow Us</h4>
  <div class="social" aria-label="Social media links"><span></span><span></span><span></span><span></span></div>
  <h4 style="left:797px">Contact Info</h4>
  <div class="contact">
    <div><svg width="12" height="16" viewBox="0 0 12 16" aria-hidden="true"><path d="M6 0 C2.7 0 0 2.6 0 5.8 C0 10 6 16 6 16 S12 10 12 5.8 C12 2.6 9.3 0 6 0 Z M6 8.2 A2.4 2.4 0 1 1 6 3.4 A2.4 2.4 0 0 1 6 8.2 Z" fill="#fff"/></svg>412 Meadow Park Lane Suite B20</div>
    <div style="padding-left:22px">Fairbrook, PA 19300</div>
    <div><svg width="13" height="14" viewBox="0 0 13 14" aria-hidden="true"><path d="M3 0 L5 4 L3.5 5.5 C4.5 8 6 9.5 8.5 10.5 L10 9 L13 11 L11.5 14 C5 13 0 8 0 1.5 Z" fill="#fff"/></svg>(555) 014-2300</div>
    <div><svg width="13" height="10" viewBox="0 0 13 10" aria-hidden="true"><rect width="13" height="10" fill="#fff"/><path d="M0 0 L6.5 5.5 L13 0" fill="none" stroke="#000" stroke-width="1.2"/></svg>hello@kelbro.com</div>
  </div>
  <div class="footer-rule"></div>
  <p class="copyright">© 2017 Company Name &nbsp;All right reserved &nbsp;Term of Use</p>
</footer>

</body>
</html>
```